Website Required for Small Cyber Security Company

Require a website for Cyber Security company. I have logo which i will attach. Please use logo blue and white as a guide
Would ultimately like the site to have a technology theme with the following pages Landing page
Services
Contact
Careers

I can provide content for each of those pages in due course, until then happy for you to use dummy data to display purposes

Target Market(s)

Government

Industry/Entity Type

Cyber Security

Coding

Coded - Design and coding required

Number of Pages Required

4 page

Colors
0054AA
0677BA
7BADD7
CADEEF
E8F1F8

Requirements
Must have
• High quality finish and UX
Nice to have
• look and feel professional and not cheap

```html
<!DOCTYPE html>
<html lang="en">
<head>
<meta charset="utf-8">
<title>Harbor Vale Consulting — Cyber Security</title>
<link rel="stylesheet" href="https://fonts.googleapis.com/css2?family=Montserrat:wght@400;500;600;700;800&display=swap">
<style>
:root{
  --blue:#0054AA;
  --blue-mid:#0677BA;
  --blue-soft:#7BADD7;
  --blue-pale:#CADEEF;
  --blue-mist:#E8F1F8;
  --navy:#1B2A5A;
  --ink:#1D2B5C;
  --text:#6B7380;
  --white:#FFFFFF;
}
*{box-sizing:border-box;margin:0;padding:0}
html,body{width:1200px;height:3466px;overflow:hidden}
body{position:relative;font-family:'Montserrat',sans-serif;color:var(--text);background:var(--white)}
.abs{position:absolute}
.media{position:absolute;display:block}

/* header */
.brand{left:150px;top:14px;width:160px;text-align:center}
.brand-mark{width:50px;height:50px;border:4px solid var(--blue-mid);border-radius:50%;margin:0 auto 6px}
.brand-name{font-size:17px;font-weight:700;color:var(--navy);line-height:1.15;letter-spacing:.3px}
.brand-name small{display:block;font-size:8px;letter-spacing:2.5px;color:var(--blue-mid)}
.nav{top:40px;left:628px;font-size:12px;font-weight:500;color:#7C8290}
.nav a{color:inherit;text-decoration:none;position:absolute;white-space:nowrap}
.nav a.active{color:var(--blue);font-weight:700}

/* hero */
.pager{left:26px;top:214px;width:30px;height:150px}
.pager span{position:absolute;left:0;transform:rotate(-90deg);font-size:13px;font-weight:600;color:var(--ink)}
.pager span.on{color:var(--blue-soft)}
.pager i{position:absolute;left:24px;top:0;width:2px;height:150px;background:var(--blue-pale)}
.pager b{position:absolute;left:24px;top:0;width:2px;height:50px;background:var(--blue-soft)}
.hero-title{left:160px;top:186px;width:380px;font-size:39px;line-height:1.0;font-weight:700;color:var(--blue)}
.hero-copy{left:160px;top:323px;width:360px;font-size:11px;line-height:1.5;text-align:justify}
.btn{position:absolute;display:flex;align-items:center;justify-content:center;gap:7px;border-radius:20px;background:var(--blue-soft);color:var(--white);font-size:11px;font-weight:600;letter-spacing:.3px}
.btn svg{width:12px;height:8px}
.frame-photo{left:547px;top:141px;width:309px;height:371px;background:var(--white);box-shadow:0 4px 16px rgba(0,0,0,.18);padding:8px}
.frame-photo .media{position:relative;width:100%;height:100%}

/* welcome */
.eyebrow{font-size:18px;font-weight:700;color:var(--blue-mid)}
.big{font-weight:800;color:var(--blue);letter-spacing:.2px}
.welcome-copy{left:642px;top:774px;width:397px;font-size:12px;line-height:1.75;text-align:justify}

/* services */
.service-card .media{position:relative;width:275px;height:307px}
.service-card h3{margin-top:14px;text-align:center;font-size:15px;font-weight:600;color:var(--blue)}
.service-card p{margin-top:6px;text-align:center;font-size:11px;font-weight:600;color:var(--blue-soft);letter-spacing:.3px}
.arrow-btn{position:absolute;width:30px;height:27px;display:flex;align-items:center;justify-content:center}

/* testimonials */
.quote{left:310px;top:1886px;width:580px;text-align:center;font-size:17.5px;line-height:1.25;color:#6F7480}
.qmark{font-size:44px;font-weight:800;color:#BFC4CC;line-height:1}
.avatar{position:absolute;border-radius:2px}

/* careers */
.acc-head{position:absolute;left:161px;width:447px;display:flex;justify-content:space-between;align-items:center;font-size:15.5px;font-weight:700;color:var(--white);padding-bottom:10px;border-bottom:1.5px solid rgba(255,255,255,.55)}
.acc-head svg{width:16px;height:16px}
.acc-body{left:161px;top:2383px;width:447px;font-size:11.5px;line-height:1.6;color:var(--white);text-align:justify}

/* contact */
.field{position:absolute;border:1px solid #9AA0AA;font-size:10px;color:#9AA0AA;padding:12px 14px}

/* footer */
.footer{left:0;top:3208px;width:1200px;height:258px;background:var(--navy);color:var(--white)}
.f-label{font-size:12px;font-weight:600}
.f-head{font-size:20px;font-weight:500;letter-spacing:.3px}
.f-line{display:flex;align-items:center;gap:8px;font-size:12.5px;font-weight:600;letter-spacing:.5px}
.social{position:absolute;width:35px;height:35px;border:2px solid var(--white);border-radius:50%}
</style>
</head>
<body>

<header>
  <div class="abs brand">
    <div class="brand-mark"></div>
    <div class="brand-name">HARBOR VALE<small>CONSULTING</small></div>
  </div>
  <nav class="abs nav">
    <a class="active" style="left:0">HOME</a>
    <a style="left:93px">SERVICES</a>
    <a style="left:213px">CAREERS</a>
    <a style="left:330px">CONTACT US</a>
  </nav>
</header>

<section class="hero">
  <div class="abs pager">
    <span style="top:8px;left:-2px" class="on">03</span>
    <span style="top:68px;left:-2px">02</span>
    <span style="top:128px;left:-2px">01</span>
    <i></i><b></b>
  </div>
  <h1 class="abs hero-title">We Provide Cyber Solutions For Your Security.</h1>
  <p class="abs hero-copy">Lorem ipsum dolor sit amet, consectetur adipiscing elit. Aenean in pharetra ligula. Praesent vestibulum a ex at vehicula. Lorem ipsum dolor sit amet, consectetur adipiscing elit. Aenean in pharetra ligula. Praesent vestibulum a ex at vehicula.</p>
  <a class="btn" style="left:161px;top:425px;width:135px;height:36px">CONTACT US
    <svg viewBox="0 0 12 8"><path d="M0 4h10M7 1l3 3-3 3" stroke="#fff" stroke-width="1.6" fill="none"/></svg></a>
  <div class="media" role="img" aria-label="Glowing blue digital padlock on a dark circuit background" style="left:664px;top:90px;width:536px;height:479px;background:radial-gradient(circle at 62% 50%,#E9F7FF 0%,#6FD3FA 10%,#1E9BE0 24%,#1466C8 40%,#0B3596 62%,#07205E 100%)"></div>
  <div class="abs frame-photo">
    <div class="media" role="img" aria-label="Businesswoman holding a protection dashboard panel" style="background:radial-gradient(ellipse at 50% 18%,#E8D2C0 0%,#C9B9AC 10%,transparent 22%),linear-gradient(180deg,#DCE2E8 0%,#C3CCD6 30%,#1A1F2A 42%,#1E5478 48%,#2A7296 70%,#163F5E 100%)"></div>
  </div>
</section>

<section class="welcome">
  <div class="media" role="img" aria-label="Isometric blue laptop with shield, fingerprint and circuit lines" style="left:0;top:596px;width:288px;height:500px;background:radial-gradient(ellipse at 45% 45%,#4A7BFF 0%,#2A52E6 25%,#1634B8 55%,#0A1E78 100%)"></div>
  <div class="media" role="img" aria-label="Woman in glasses typing on a laptop beside a brick wall" style="left:297px;top:646px;width:307px;height:412px;background:radial-gradient(ellipse at 48% 62%,#151518 0%,#222 30%,transparent 48%),linear-gradient(90deg,#8A5444 0%,#6B4235 35%,#3A3A3E 70%,#1A1A1C 100%)"></div>
  <div class="abs eyebrow" style="left:642px;top:680px">WELCOME TO</div>
  <div class="abs big" style="left:641px;top:702px;font-size:33px">HARBOR VALE</div>
  <div class="abs" style="left:642px;top:740px;font-size:13px;letter-spacing:13px;color:var(--blue-mid)">CONSULTING</div>
  <p class="abs welcome-copy">At Stoneridge Builders, we specialize in transforming houses into homes. From kitchen and bathroom remodeling to home additions and outdoor spaces, we have the expertise to bring your vision to life. Our skilled team of carpenters is committed to providing excellent craftsmanship, smart solutions, and professional service at fair and reasonable costs. With a focus on integrity and ethical business practices, we ensure open communication and superior quality workmanship.</p>
  <a class="btn" style="left:642px;top:973px;width:127px;height:34px">READ MORE
    <svg viewBox="0 0 12 8"><path d="M0 4h10M7 1l3 3-3 3" stroke="#fff" stroke-width="1.6" fill="none"/></svg></a>
</section>

<section class="services abs" style="left:0;top:1096px;width:1200px;height:632px;background:var(--blue-mist)">
  <div class="abs eyebrow" style="left:162px;top:67px">OUR SERVICES</div>
  <h2 class="abs big" style="left:159px;top:96px;font-size:40px;line-height:1.05">CYBER SECURITY<br>SOLUTIONS</h2>
  <p class="abs" style="left:604px;top:101px;width:325px;font-size:11.5px;line-height:1.3;color:#555C68">At Stoneridge Builders, we offer a<br>comprehensive range of services to cater to all your remodeling needs.</p>
  <div class="arrow-btn" style="left:968px;top:94px;border:1px solid var(--blue-pale);background:var(--white)">
    <svg width="14" height="8" viewBox="0 0 14 8"><path d="M14 4H2M5 1 2 4l3 3" stroke="#555C68" stroke-width="1.4" fill="none"/></svg></div>
  <div class="arrow-btn" style="left:1008px;top:94px;background:var(--blue-soft)">
    <svg width="14" height="8" viewBox="0 0 14 8"><path d="M0 4h12M9 1l3 3-3 3" stroke="#fff" stroke-width="1.4" fill="none"/></svg></div>

  <article class="abs service-card" style="left:161px;top:211px">
    <div class="media" role="img" aria-label="Yellow folder secured with a steel padlock" style="background:radial-gradient(ellipse at 42% 50%,#E7D94A 0%,#D9C83A 22%,transparent 42%),radial-gradient(ellipse at 70% 70%,#6E6E6E 0%,#9A9A9A 18%,transparent 34%),linear-gradient(160deg,#F1F1F1 0%,#DCDCDC 55%,#C9C9C9 100%)"></div>
    <h3>Folder Security</h3><p>READ MORE &#10230;</p>
  </article>
  <article class="abs service-card" style="left:463px;top:211px">
    <div class="media" role="img" aria-label="Isometric server tower linked to laptops" style="background:radial-gradient(ellipse at 50% 50%,#8E9AF0 0%,#5B5FD6 15%,#33289A 36%,#1E1468 70%,#170F55 100%)"></div>
    <h3>Server Security</h3><p>READ MORE &#10230;</p>
  </article>
  <article class="abs service-card" style="left:764px;top:211px">
    <div class="media" role="img" aria-label="Cloud with documents and upload and download arrows" style="background:radial-gradient(ellipse at 48% 48%,#FFFFFF 0%,#F2F8FC 18%,#7EB4DC 30%,#B5DEF0 46%,#C3E6F5 100%)"></div>
    <h3>File Dulication</h3><p>READ MORE &#10230;</p>
  </article>
</section>

<section class="testimonials">
  <div class="abs eyebrow" style="left:0;width:1200px;text-align:center;top:1779px">CLIENT SAYS</div>
  <h2 class="abs big" style="left:0;width:1200px;text-align:center;top:1800px;font-size:39px">TESTIMONIALS</h2>
  <div class="abs qmark" style="left:270px;top:1872px">&ldquo;</div>
  <p class="abs quote">Quis autem vel eum iure reprehenderit aui in ea voluptate velit esse quam nihil molestiae consequatur, vel illum qui dolorem eum fugiat voluptas pariatur.</p>
  <div class="abs qmark" style="left:878px;top:1960px">&rdquo;</div>
  <div class="avatar" role="img" aria-label="Client portrait" style="left:495px;top:2000px;width:58px;height:55px;background:linear-gradient(180deg,#EEF0F2 0%,#C9B8A8 50%,#E4E7EB 100%)"></div>
  <div class="avatar" role="img" aria-label="Client portrait" style="left:561px;top:1978px;width:78px;height:77px;background:linear-gradient(180deg,#F4F5F7 0%,#B99A86 40%,#4E86C8 70%,#3C74B8 100%)"></div>
  <div class="avatar" role="img" aria-label="Client portrait" style="left:647px;top:2000px;width:58px;height:55px;background:linear-gradient(180deg,#EDEDEE 0%,#8A6A58 45%,#D6D2CF 100%)"></div>
  <div class="abs" style="left:0;width:1200px;text-align:center;top:2068px;font-size:13.5px;font-weight:700;color:var(--ink)">MARIN DELLOW</div>
  <div class="abs" style="left:0;width:1200px;text-align:center;top:2087px;font-size:11px;color:#8A909A">LORUM IPSLUM</div>
</section>

<section class="careers abs" style="left:0;top:2147px;width:1200px;height:601px;background:var(--blue-soft)">
  <h2 class="abs big" style="left:0;width:1200px;text-align:center;top:48px;font-size:40px;color:var(--white)">CAREERS</h2>
  <p class="abs" style="left:330px;width:540px;text-align:center;top:104px;font-size:11.5px;line-height:1.3;color:var(--white)">At Stoneridge Builders, we offer a comprehensive range of services to cater to<br>all your remodeling needs Builders we offer a comprehe.</p>
</section>
<div class="acc-head" style="top:2326px">LOREM IPSUM DOLOR SIT
  <svg viewBox="0 0 16 16"><circle cx="8" cy="8" r="8" fill="#fff"/><path d="M4.5 6.5 8 10l3.5-3.5" stroke="#7BADD7" stroke-width="1.8" fill="none"/></svg></div>
<p class="abs acc-body">Lorem ipsum dolor sit amet, consectetur adipiscing elit. Cras tempus ullamcorper ultrices. Vestibulum gravida diam sed commodo volutpat. Nunc porttitor lorem mauris, nec varius justo vehicula quis. Sed pulvinar lectus eget ipsum scelerisque elementum.</p>
<div class="acc-head" style="top:2485px">LOREM IPSUM DOLOR SIT
  <svg viewBox="0 0 16 16"><circle cx="8" cy="8" r="8" fill="#fff"/><path d="M6.5 4.5 10 8l-3.5 3.5" stroke="#7BADD7" stroke-width="1.8" fill="none"/></svg></div>
<div class="acc-head" style="top:2539px">LOREM IPSUM DOLOR SIT
  <svg viewBox="0 0 16 16"><circle cx="8" cy="8" r="8" fill="#fff"/><path d="M6.5 4.5 10 8l-3.5 3.5" stroke="#7BADD7" stroke-width="1.8" fill="none"/></svg></div>
<a class="btn" style="left:161px;top:2611px;width:163px;height:54px;border-radius:28px;background:var(--blue);font-size:15px;font-weight:700">VIEW DETAILS</a>
<div class="abs" style="left:659px;top:2313px;width:381px;height:351px;background:var(--white);padding:8px">
  <div class="media" role="img" aria-label="Two smiling professionals in suits, one holding a clipboard" style="position:relative;width:100%;height:100%;background:radial-gradient(ellipse at 30% 22%,#D9B59C 0%,#C8A48C 8%,transparent 16%),radial-gradient(ellipse at 68% 30%,#D3AE95 0%,#BE9A82 7%,transparent 14%),linear-gradient(180deg,#C4CBD3 0%,#A3ACB7 32%,#2A2E36 52%,#1C1F25 100%)"></div>
</div>

<section class="contact">
  <div class="abs eyebrow" style="left:161px;top:2813px;color:var(--blue)">GET IN TOUCH</div>
  <h2 class="abs" style="left:160px;top:2836px;font-size:40px;font-weight:800;color:var(--ink)">CONTACT US</h2>
  <p class="abs" style="left:566px;top:2834px;width:470px;font-size:11.5px;line-height:1.3;color:#8A909A">Lorem ipsum dolor sit amet, consectetur adipiscing elit. Cras tempus ullamcorper ultrices. Vestibulum gravida diam sed commodo volutpat. Nunc porttitor lorem mauris.</p>
  <div class="field" style="left:161px;top:2903px;width:282px;height:44px">Name</div>
  <div class="field" style="left:460px;top:2903px;width:281px;height:44px">E-Mail</div>
  <div class="field" style="left:759px;top:2903px;width:280px;height:44px">Phone</div>
  <div class="field" style="left:161px;top:2962px;width:878px;height:114px">Message</div>
  <a class="btn" style="left:511px;top:3099px;width:178px;height:42px;border-radius:22px;background:var(--blue);font-size:13px;font-weight:700;gap:30px">SUBMIT
    <svg viewBox="0 0 12 8"><path d="M0 4h10M7 1l3 3-3 3" stroke="#fff" stroke-width="1.6" fill="none"/></svg></a>
</section>

<footer class="abs footer">
  <div class="abs" style="left:160px;top:52px">
    <div class="f-label">Contact</div>
    <div class="f-head">DETAILS</div>
    <div class="f-line" style="margin-top:18px">
      <svg width="12" height="12" viewBox="0 0 24 24"><path fill="#fff" d="M6.6 10.8a15 15 0 0 0 6.6 6.6l2.2-2.2c.3-.3.7-.4 1-.2 1.1.4 2.3.6 3.6.6.6 0 1 .4 1 1V20c0 .6-.4 1-1 1A17 17 0 0 1 3 4c0-.6.4-1 1-1h3.5c.6 0 1 .4 1 1 0 1.3.2 2.5.6 3.6.1.3 0 .7-.2 1z"/></svg>
      + 1 (555) 014-2278</div>
    <div class="f-line" style="margin-top:6px">
      <svg width="13" height="11" viewBox="0 0 13 11"><rect x=".7" y=".7" width="11.6" height="9.6" fill="none" stroke="#fff" stroke-width="1.3"/><path d="M.7 .9 6.5 6l5.8-5.1" fill="none" stroke="#fff" stroke-width="1.3"/></svg>
      info@harborvale.com</div>
  </div>
  <div class="abs" style="left:433px;top:67px;width:1px;height:94px;background:rgba(255,255,255,.2)"></div>
  <div class="abs" style="left:508px;top:52px">
    <div class="f-label">Follow us</div>
    <div class="f-head">SOCIAL MEDIA</div>
  </div>
  <span class="social" role="img" aria-label="Social profile link" style="left:508px;top:105px"></span>
  <span class="social" role="img" aria-label="Social profile link" style="left:552px;top:105px"></span>
  <span class="social" role="img" aria-label="Social profile link" style="left:597px;top:105px"></span>
  <div class="abs" style="left:744px;top:67px;width:1px;height:94px;background:rgba(255,255,255,.2)"></div>
  <div class="abs" style="left:812px;top:52px">
    <div class="f-label">Follow our</div>
    <div class="f-head">LOCATION</div>
    <div class="f-line" style="margin-top:16px">
      <svg width="8" height="11" viewBox="0 0 8 11"><path fill="#fff" d="M4 0a4 4 0 0 1 4 4c0 3-4 7-4 7S0 7 0 4a4 4 0 0 1 4-4zm0 2.5a1.5 1.5 0 1 0 0 3 1.5 1.5 0 0 0 0-3z"/></svg>
      Harbor Vale</div>
    <div style="margin-left:14px;font-size:12px;margin-top:3px">PO Box 1180 Millbrook, NC 27000</div>
  </div>
  <div class="abs" style="left:160px;top:191px;width:878px;height:1px;background:rgba(255,255,255,.15)"></div>
  <div class="abs" style="left:0;width:1200px;text-align:center;top:211px;font-size:12.5px;font-weight:600">©2023 HARBOR VALE. ALL RIGHTS RESERVED.</div>
</footer>

</body>
</html>
```